Silent Disco and Photo Booth Magazine Advertisements

We have two one-page advertisement placements in a magazine that is being distributed to thousands of people at a large Christian camp. We are targeting all the folks reading the ad, but especially want this catered to Youth Pastors, who are the ones who would make the buying decision on renting equipment from us. They need to have the exact same feel and vibe, hence being made together here.

We want one of these full-page advertisements to feature our Silent Disco Headsets, and the other to be focused on our Photo Booths. Our company rents and ships event equipment nationally as our primary service, and we want to feature that as the focus.

We are a fun company, provide fun entertainment equipment services, and take a 100% satisfaction approach to our customer service. We have a long-standing reputation for providing equipment that will be a guaranteed successful event and always arrive on time. It's easy, fun, and a fair value.

Attached are two mock-ups of some ideas we have around it. Some content options are below:

***Silent Disco Rentals***
Rentals starting at $5 per person (plus the cost of shipping)
Easy to setup
Works well for prayer and for silent disco fun
Guarantee to get everyone out for a fun time
Nation's biggest silent disco provider
50 or 5,000 we got you covered
Go to quietgroovehire.com/experiences/church/ to find our youth pastor event guide

**Photo booth**
Shippability (national)
Portability (very portable)
Setup in 5 minutes
Social fun aspect
Social sharing aspect (PicShare/FriendNet)
Full branding: Use for contests, promotions, special sponsorships
KELNA special starting at $679 (crossed out $479) for 2022
Save $200 off of every order

PLEASE USE THESE COLORS:
Colors:
Pink- HEX #CC008F
HEX # 690065
Black- HEX #000000

Font:
Font- Montserrat (Primary)
Roboto (Secondary)

Target Market(s)

Youth Pastors, Pastors, Church Event Managers, Church Activity Directors 18-40 years old

Font styles to use
Other font styles liked:
• Font- Montserrat (Primary) Roboto (Secondary) (Pink- HEX #CC008F HEX # 690065 Black- HEX #000000)

Colors

Designer to choose colors to be used in the design.

Requirements
Must have
• Crisp, clear, call to action, explanation of offerings, great theme. Font- Montserrat (Primary) Roboto (Secondary) Pink- HEX #CC008F HEX # 690065 Black- HEX #000000

```html
<!DOCTYPE html>
<html lang="en">
<head>
<meta charset="utf-8">
<title>QuietGroove Hire – Silent Disco &amp; Photo Booth Rentals</title>
<link href="https://fonts.googleapis.com/css2?family=Montserrat:wght@300;400;500;600;700&display=swap" rel="stylesheet">
<style>
  :root{
    --pink:#cc008f;
    --plum:#690065;
    --ink:#000000;
    --charcoal:#26262b;
    --text-grey:#3a3a3a;
    --soft-grey:#6d6d70;
    --page:#c9c9cb;
    --white:#ffffff;
  }
  *{margin:0;padding:0;box-sizing:border-box}
  html,body{width:1200px;height:2400px;overflow:hidden;background:var(--page)}
  body{position:relative;font-family:"Montserrat",Arial,sans-serif}

  .ad{position:absolute;left:50px;top:488px;width:1100px;height:1424px;overflow:hidden;
      background:var(--charcoal);box-shadow:0 14px 40px rgba(0,0,0,.35)}

  .concert-photo{position:absolute;left:0;top:0;width:1100px;height:560px;
      background:
        radial-gradient(ellipse at 50% 18%, rgba(120,220,210,.55), transparent 45%),
        radial-gradient(ellipse at 12% 25%, rgba(70,120,230,.55), transparent 30%),
        radial-gradient(ellipse at 88% 25%, rgba(70,120,230,.5), transparent 30%),
        linear-gradient(180deg,#1a1d2c 0%,#3a2a33 45%,#5a1a22 70%,#222 100%)}

  .content-panel{position:absolute;left:0;top:380px;width:1100px;height:890px;
      background:linear-gradient(90deg, rgba(38,38,43,1) 0%, rgba(38,38,43,1) 34%, rgba(240,240,242,1) 52%, #ffffff 70%);}
  .content-panel::before{content:"";position:absolute;inset:0;
      background:linear-gradient(180deg, rgba(38,38,43,0) 0%, rgba(255,255,255,0) 40%);}
  .panel-fade{position:absolute;left:0;top:380px;width:1100px;height:200px;
      background:linear-gradient(180deg, rgba(38,38,43,0) 0%, rgba(255,255,255,0) 100%)}

  .booth-photo{position:absolute;left:92px;top:278px;width:320px;height:1020px;
      border-radius:160px 160px 6px 6px;
      background:
        radial-gradient(circle at 50% 155px, #8a8a8c 0 90px, #ffffff 92px 150px, transparent 152px),
        linear-gradient(180deg, transparent 0 300px, #111 300px 1020px)}

  .round-photo{position:absolute;border-radius:50%;}
  .round-photo--ringlight{left:649px;top:312px;width:184px;height:184px;border:5px solid var(--pink);
      background:radial-gradient(circle at 35% 40%, #e8e8ea, #6a6a72 55%, #2c2c30)}
  .round-photo--headsets{left:821px;top:272px;width:242px;height:242px;border:8px solid #d7d7da;
      background:radial-gradient(circle, #b0179a 0 45%, var(--pink) 70%, var(--plum) 100%)}

  .banner{position:absolute;left:465px;width:597px;height:56px}
  .banner svg{position:absolute;inset:0}
  .banner h2{position:absolute;right:54px;top:6px;color:var(--white);font-weight:600;font-size:37px;letter-spacing:.3px}
  .banner--disco{top:547px}
  .banner--booth{top:903px}

  .right{position:absolute;right:60px;text-align:right}
  .offer{color:var(--pink);font-weight:700;font-size:23px;line-height:27px}
  .offer s{text-decoration-thickness:2px}
  .features{list-style:none;right:54px}
  .features li{font-size:21px;font-weight:400;color:var(--text-grey);line-height:26px;padding-right:34px;position:relative}
  .features li svg{position:absolute;right:0;top:5px;width:17px;height:17px}
  .guide{font-size:21px;color:var(--soft-grey);line-height:26px}
  .guide a{color:var(--pink);text-decoration:none;font-weight:500}
  .branding-label{color:var(--pink);font-weight:600;font-size:21px;line-height:26px}

  .footer-curve{position:absolute;left:0;top:1230px;width:1100px;height:60px}
  .footer{position:absolute;left:0;top:1270px;width:1100px;height:154px;background:var(--charcoal)}

  .brand{position:absolute;left:92px;top:30px;display:flex;align-items:center;gap:16px}
  .brand-dot{width:42px;height:42px;border-radius:50%;background:#c7c7c9}
  .brand-name{color:#c7c7c9;font-weight:700;font-size:38px;line-height:44px;letter-spacing:1px}

  .cta{position:absolute;right:60px;top:22px;text-align:right}
  .cta h3{color:var(--pink);font-weight:600;font-size:32px;line-height:40px}
  .cta p{color:var(--white);font-size:20px;line-height:36px;padding-right:30px;position:relative}
  .cta p svg{position:absolute;right:0;top:10px;width:17px;height:17px}
</style>
</head>
<body>
<main class="ad">
  <div class="concert-photo" role="img" aria-label="Photo of a silent disco crowd in front of a lit stage with DJs"></div>
  <div class="content-panel"></div>

  <div class="booth-photo" role="img" aria-label="Photo of a selfie station photo booth with ring light on a black stand"></div>

  <div class="round-photo round-photo--ringlight" role="img" aria-label="Photo of a guest using the ring light booth"></div>
  <div class="round-photo round-photo--headsets" role="img" aria-label="Photo of three silent disco headsets"></div>

  <section class="banner banner--disco">
    <svg viewBox="0 0 597 56" preserveAspectRatio="none"><polygon points="40,0 597,0 557,56 0,56" fill="var(--pink)"/></svg>
    <h2>SILENT DISCO RENTALS</h2>
  </section>
  <p class="right offer" style="top:622px">RENTALS STARTING AT $5 PER PERSON<br>(plus the cost of shipping)</p>
  <ul class="right features" style="top:684px">
    <li>Easy to setup<svg viewBox="0 0 20 20"><circle cx="10" cy="10" r="8.5" fill="none" stroke="var(--pink)" stroke-width="1.5"/><path d="M12 6 8 10l4 4" fill="none" stroke="var(--pink)" stroke-width="1.8"/></svg></li>
    <li>Works well for prayer and for silent disco fun<svg viewBox="0 0 20 20"><circle cx="10" cy="10" r="8.5" fill="none" stroke="var(--pink)" stroke-width="1.5"/><path d="M12 6 8 10l4 4" fill="none" stroke="var(--pink)" stroke-width="1.8"/></svg></li>
    <li>Guarantee to get everyone out for a fun time<svg viewBox="0 0 20 20"><circle cx="10" cy="10" r="8.5" fill="none" stroke="var(--pink)" stroke-width="1.5"/><path d="M12 6 8 10l4 4" fill="none" stroke="var(--pink)" stroke-width="1.8"/></svg></li>
    <li>Nation's biggest silent disco provider<svg viewBox="0 0 20 20"><circle cx="10" cy="10" r="8.5" fill="none" stroke="var(--pink)" stroke-width="1.5"/><path d="M12 6 8 10l4 4" fill="none" stroke="var(--pink)" stroke-width="1.8"/></svg></li>
    <li>50 or 5,000 we got you covered<svg viewBox="0 0 20 20"><circle cx="10" cy="10" r="8.5" fill="none" stroke="var(--pink)" stroke-width="1.5"/><path d="M12 6 8 10l4 4" fill="none" stroke="var(--pink)" stroke-width="1.8"/></svg></li>
  </ul>
  <p class="right guide" style="top:829px">Go to <a>quietgroovehire.com/experiences/church/</a><br>to find our youth pastor event guide</p>

  <section class="banner banner--booth">
    <svg viewBox="0 0 597 56" preserveAspectRatio="none"><polygon points="40,0 597,0 557,56 0,56" fill="var(--pink)"/></svg>
    <h2>PHOTO BOOTH RENTALS</h2>
  </section>
  <p class="right offer" style="top:975px">KELNA SPECIAL STARTING AT $679 <s>$479</s> FOR 2022<br>SAVE $200 OFF OF EVERY ORDER</p>
  <ul class="right features" style="top:1036px">
    <li>Shippability (national)<svg viewBox="0 0 20 20"><circle cx="10" cy="10" r="8.5" fill="none" stroke="var(--pink)" stroke-width="1.5"/><path d="M12 6 8 10l4 4" fill="none" stroke="var(--pink)" stroke-width="1.8"/></svg></li>
    <li>Portability (very portable)<svg viewBox="0 0 20 20"><circle cx="10" cy="10" r="8.5" fill="none" stroke="var(--pink)" stroke-width="1.5"/><path d="M12 6 8 10l4 4" fill="none" stroke="var(--pink)" stroke-width="1.8"/></svg></li>
    <li>Setup in 5 minutes<svg viewBox="0 0 20 20"><circle cx="10" cy="10" r="8.5" fill="none" stroke="var(--pink)" stroke-width="1.5"/><path d="M12 6 8 10l4 4" fill="none" stroke="var(--pink)" stroke-width="1.8"/></svg></li>
    <li>Social fun aspect<svg viewBox="0 0 20 20"><circle cx="10" cy="10" r="8.5" fill="none" stroke="var(--pink)" stroke-width="1.5"/><path d="M12 6 8 10l4 4" fill="none" stroke="var(--pink)" stroke-width="1.8"/></svg></li>
    <li>Social sharing aspect (PicShare/FriendNet)<svg viewBox="0 0 20 20"><circle cx="10" cy="10" r="8.5" fill="none" stroke="var(--pink)" stroke-width="1.5"/><path d="M12 6 8 10l4 4" fill="none" stroke="var(--pink)" stroke-width="1.8"/></svg></li>
  </ul>
  <p class="right branding-label" style="top:1178px;right:66px">Full branding:</p>
  <p class="right guide" style="top:1204px">Use for contests, promotions, special sponsorships</p>

  <svg class="footer-curve" viewBox="0 0 1100 60" preserveAspectRatio="none">
    <path d="M250 60 C 270 38, 290 36, 330 36 L1100 36 L1100 60 Z" fill="var(--charcoal)"/>
    <path d="M250 60 C 270 38, 290 36, 330 36 L1100 36" fill="none" stroke="var(--pink)" stroke-width="6"/>
  </svg>

  <footer class="footer">
    <div class="brand">
      <span class="brand-dot"></span>
      <span class="brand-name">QUIETGROOVE<br>HIRE.COM</span>
    </div>
    <div class="cta">
      <h3>RENT WITH US TODAY!</h3>
      <p>1 (833) QGROOVE | 1 (833) 555-0147<svg viewBox="0 0 20 20"><circle cx="10" cy="10" r="9" fill="var(--pink)"/><path d="M6.5 5.5c.8-.6 1.5-.4 2 .5l.6 1.3c.2.5 0 1-.4 1.3l-.5.4c.6 1.3 1.5 2.2 2.8 2.8l.4-.5c.3-.4.8-.6 1.3-.4l1.3.6c.9.5 1.1 1.2.5 2-1 1.3-2.8 1.3-5-.6-2.3-2.1-3.9-5-3-7.4z" fill="var(--white)"/></svg></p>
      <p>WWW.QUIETGROOVEHIRE.COM<svg viewBox="0 0 20 20"><circle cx="10" cy="10" r="8" fill="none" stroke="var(--pink)" stroke-width="1.8"/><ellipse cx="10" cy="10" rx="3.5" ry="8" fill="none" stroke="var(--pink)" stroke-width="1.5"/><path d="M2 10h16" stroke="var(--pink)" stroke-width="1.5"/></svg></p>
    </div>
  </footer>
</main>
</body>
</html>
```